VR Business Card

Design new business cards for VELMOsoft

Please see attached for the design brief

**** Please note, please feel free to propose a font that works for a professional, technology company ***

Target Market(s)

Technology buyers

Industry/Entity Type

Business

```html
<!DOCTYPE html>
<html lang="en">
<head>
<meta charset="utf-8">
<title>VELMOsoft Business Cards</title>
<link rel="stylesheet" href="https://fonts.googleapis.com/css2?family=Roboto+Condensed:wght@300;400&display=swap">
<style>
  :root {
    --backdrop: #1b1b1c;
    --card: #262627;
    --card-sheen: #3a3a3c;
    --text-light: #d9d9d9;
    --text-muted: #9a9a9a;
    --accent-orange: #f0a43a;
    --band-blue: #3d62a8;
    --band-orange: #e39a2c;
    --band-teal: #1f6b5e;
    --band-purple: #3f3f86;
    --marker-grey: #6a6a6e;
  }
  * { margin: 0; padding: 0; box-sizing: border-box; }
  html, body {
    width: 900px; height: 1200px; overflow: hidden;
    background: var(--backdrop);
    font-family: "Roboto Condensed", Arial, sans-serif;
  }
  .card {
    position: absolute; left: 130px;
    width: 640px; height: 366px;
    background: linear-gradient(125deg, var(--card) 0%, var(--card-sheen) 45%, var(--card) 75%);
    box-shadow: 0 18px 40px rgba(0,0,0,.6);
    overflow: hidden;
  }
  .card--front { top: 160px; }
  .card--back { top: 680px; }

  .brand {
    position: absolute; left: 56px; top: 176px;
    display: flex; align-items: center; gap: 14px;
  }
  .brand__marker { width: 14px; height: 14px; border-radius: 50%; background: var(--marker-grey); }
  .brand__name {
    font-size: 40px; font-weight: 300; color: var(--text-light);
    letter-spacing: 1px; line-height: 1;
  }

  .company, .contact {
    position: absolute; left: 380px; top: 54px;
    font-size: 15px; line-height: 20px; color: var(--text-light);
  }
  .company__name, .contact__name { color: var(--accent-orange); font-size: 17px; margin-bottom: 4px; }
  .company__web {
    margin-top: 8px; font-size: 11px; letter-spacing: 4px; color: var(--text-muted);
  }
  .contact__role { font-size: 13px; color: var(--text-muted); margin-bottom: 10px; }
  .contact__row { display: flex; align-items: center; gap: 10px; line-height: 21px; }
  .contact__row svg { width: 13px; height: 13px; fill: var(--text-light); flex: none; }

  .tagline {
    position: absolute; right: 36px; bottom: 36px;
    font-size: 15px; letter-spacing: 6px; color: var(--accent-orange);
    white-space: nowrap;
  }

  .edge-bands {
    position: absolute; left: 0; bottom: 0; width: 100%; height: 12px;
    display: flex;
  }
  .edge-bands span { flex: 1; }
  .band--blue { background: var(--band-blue); }
  .band--orange { background: var(--band-orange); }
  .band--teal { background: var(--band-teal); }
  .band--purple { background: var(--band-purple); }
</style>
</head>
<body>

<section class="card card--front">
  <div class="brand">
    <span class="brand__marker"></span>
    <span class="brand__name">VELMOsoft</span>
  </div>
  <div class="company">
    <div class="company__name">VELMOsoft Solutions AG</div>
    <div>Lindenweg 8</div>
    <div>4410 Aldermoor</div>
    <div>Westland</div>
    <div class="company__web">www.velmosoft-it.com</div>
  </div>
  <div class="edge-bands">
    <span class="band--blue"></span><span class="band--orange"></span><span class="band--teal"></span><span class="band--purple"></span>
  </div>
</section>

<section class="card card--back">
  <div class="brand">
    <span class="brand__marker"></span>
    <span class="brand__name">VELMOsoft</span>
  </div>
  <div class="contact">
    <div class="contact__name">Martin Hollen</div>
    <div class="contact__role">CEO</div>
    <div class="contact__row">
      <svg viewBox="0 0 16 16" aria-hidden="true"><path d="M3 1l3 3-1.5 2a9 9 0 0 0 5.5 5.5L12 10l3 3-2 2C7 15 1 9 1 3z"/></svg>
      <span>+41 41 555 0142</span>
    </div>
    <div class="contact__row">
      <svg viewBox="0 0 16 16" aria-hidden="true"><path d="M2 5h12v9H2zM4 1h8v3H4z"/></svg>
      <span>+41 800 555 019</span>
    </div>
    <div class="contact__row">
      <svg viewBox="0 0 16 16" aria-hidden="true"><path d="M4 1h8v14H4zm2 2v9h4V3z"/></svg>
      <span>+41 78 555 2671</span>
    </div>
    <div class="contact__row">
      <svg viewBox="0 0 16 16" aria-hidden="true"><path d="M1 3h14v10H1zm1.5 1.5L8 9l5.5-4.5z"/></svg>
      <span>martin.hollen@velmosoft-it.com</span>
    </div>
  </div>
  <div class="tagline">...ideas set in motion</div>
  <div class="edge-bands">
    <span class="band--blue"></span><span class="band--orange"></span><span class="band--teal"></span><span class="band--purple"></span>
  </div>
</section>

</body>
</html>
```